Business Card Design Project - Small Bar

We would like a design for a business card for our new small bar in Melbourne. It is quite the 'hipster' bar and the card would need to reflect this in its design. We do have a logo which needs to be used in the card, tho how it is incorporated is up to you! :)

OK, the Bar currently has a common 'inner city' vibe, i.e. random artwork, older 30s/40's club furniture, grafitti murals on the walls, eclectic objects etc etc Current clientele would be described as "hipster", "urban professional" etc. How to describe... they are 30, have a good job but have beards, beanies and own vinyl records. :)

The card will be used to give to professional contacts and to bands/solo artists we come across to invite them to come play at our venue, so somehow I would like it to convey the image of 'professional' and 'funky' all in one. Difficult I know.

I have asked for some advice on making this brief clearer, so check back.

Thanks all in advance. :)
Updates

Sorry all

I've now been told that it is WEST MELBOURNE 3003. Apparently we are on the border and it is referred to by either west or north Melbourne, but it is definitely West Melbourne 3003.

Things you learn hey? :)

Target Market(s)

Hipsters, urbanites, the inner city crowd

Industry/Entity Type

Artists

Requirements
Must have
• Logo (JPG file attached)
Name of the bar "The Lantern & Otter"
Address - 742 Brindle St, North Melbourne, Victoria 3051
Names - Owen Partridge, Lewis Dunhurst
mobile. 0417265093 and 0456302714
Obviously we would need separate cards?
Nice to have
• Pagebook link
Pagebook 'like' icon
Should not have
• traditional designs. I am looking for something unique and funky. with FUNK! :)

```html
<!DOCTYPE html>
<html lang="en">
<head>
<meta charset="utf-8">
<title>The Lantern &amp; Otter — Business Card</title>
<link rel="stylesheet" href="https://fonts.googleapis.com/css2?family=Josefin+Sans:wght@300;400&display=swap">
<style>
  :root {
    --page: #ffffff;
    --ink: #1a1a1a;
    --card-edge: #3a3a3a;
    --accent-red: #e0352b;
    --accent-blue: #2a3f8f;
    --navy: #25346e;
    --teal: #6fd6c8;
    --social-blue: #2f5fb8;
    --social-sky: #3fb6e8;
    --social-red: #c8261f;
  }
  * { margin: 0; padding: 0; box-sizing: border-box; }
  html, body { width: 1200px; height: 877px; overflow: hidden; background: var(--page); }
  body { position: relative; font-family: "Josefin Sans", sans-serif; font-weight: 300; color: var(--ink); }

  .card {
    position: absolute; top: 50px; width: 496px; height: 768px;
    border: 1.5px solid var(--card-edge); border-radius: 36px; background: var(--page); overflow: hidden;
  }
  .card--front { left: 52px; }
  .card--back { left: 625px; }

  .front-artwork {
    position: absolute; left: 36px; top: 70px; width: 440px; height: 650px;
    background:
      radial-gradient(ellipse at 55% 35%, var(--accent-red) 0%, rgba(224,53,43,0) 45%),
      radial-gradient(ellipse at 60% 65%, var(--teal) 0%, rgba(111,214,200,0) 45%),
      radial-gradient(ellipse at 30% 50%, var(--navy) 0%, rgba(37,52,110,0) 55%),
      radial-gradient(ellipse at 50% 50%, #9aa0a8 0%, rgba(255,255,255,0) 70%);
  }
  .front-wordmark {
    position: absolute; left: 70px; top: 86px; z-index: 1;
    display: flex; align-items: center; gap: 8px; white-space: nowrap;
    font-size: 18px; font-weight: 400; color: var(--ink);
  }
  .front-wordmark-dot { width: 14px; height: 14px; border-radius: 50%; background: var(--ink); }

  .back-content { position: absolute; inset: 0; text-align: center; }
  .wordmark {
    position: absolute; top: 100px; left: 0; right: 0;
    display: flex; justify-content: center; align-items: center; gap: 12px;
    font-size: 24px; font-weight: 400; color: var(--ink); white-space: nowrap;
  }
  .wordmark-dot { width: 20px; height: 20px; border-radius: 50%; background: var(--ink); }

  .person-name { position: absolute; top: 196px; left: 0; right: 0; font-size: 46px; font-weight: 300; }
  .venue-name { position: absolute; top: 256px; left: 0; right: 0; font-size: 38px; color: var(--accent-red); }
  .mobile { position: absolute; top: 310px; left: 0; right: 0; font-size: 48px; letter-spacing: 1px; }
  .address { position: absolute; top: 472px; left: 0; right: 0; font-size: 25px; line-height: 38px; }
  .tagline { position: absolute; top: 560px; left: 0; right: 0; font-size: 36px; color: var(--accent-blue); }

  .social-list {
    position: absolute; top: 624px; left: 14px; right: 14px;
    display: flex; justify-content: space-between; list-style: none;
  }
  .social-item { display: flex; flex-direction: column; align-items: center; gap: 4px; width: 110px; font-size: 13px; font-weight: 400; white-space: nowrap; }
  .social-dot { width: 56px; height: 56px; border-radius: 50%; }
  .social-item--page .social-dot { background: var(--social-blue); }
  .social-item--chirp .social-dot { background: var(--social-sky); }
  .social-item--reel .social-dot { background: var(--social-red); }
  .social-item--circle .social-dot { background: var(--accent-red); }

  .handle { position: absolute; top: 714px; left: 0; right: 0; font-size: 36px; font-weight: 300; white-space: nowrap; }
</style>
</head>
<body>
  <section class="card card--front">
    <div class="front-artwork" role="img" aria-label="Graffiti-style spray-paint artwork in navy, red and teal with hand lettering of the bar name"></div>
    <span class="front-wordmark"><span class="front-wordmark-dot"></span>The Lantern &amp; Otter</span>
  </section>

  <section class="card card--back">
    <div class="back-content">
      <div class="wordmark"><span class="wordmark-dot"></span>The Lantern &amp; Otter</div>
      <h1 class="person-name">Owen Partridge</h1>
      <p class="venue-name">The Lantern and Otter</p>
      <p class="mobile">M: 0417265093</p>
      <p class="address">742 Brindle St, North Melbourne,<br>Victoria 3051</p>
      <p class="tagline">Light Us Home</p>
      <ul class="social-list">
        <li class="social-item social-item--page"><span class="social-dot"></span>Pagebook</li>
        <li class="social-item social-item--chirp"><span class="social-dot"></span>Chirper</li>
        <li class="social-item social-item--reel"><span class="social-dot"></span>Reelcast</li>
        <li class="social-item social-item--circle"><span class="social-dot"></span>Circleplus</li>
      </ul>
      <p class="handle">thelanternandotter</p>
    </div>
  </section>
</body>
</html>
```